Copperleaf Grill
there is none
Copperleaf Grill -
Simple
Danielle Whitcomb
Proprietor
318 Ferrand Street New Orleans, LA 70119
dwhitcomb@copperleaf-eats.com
www.copperleaf-eats.com
Use the same font of Grill and New Orleans for information on card
Just put the logo and website on the back of the card

```html
<!DOCTYPE html>
<html lang="en">
<head>
<meta charset="utf-8">
<title>Copperleaf Grill – Business Cards</title>
<link rel="stylesheet" href="https://fonts.googleapis.com/css2?family=Montserrat:wght@400;500;600&display=swap">
<style>
  :root {
    --maroon: #8a2b3b;
    --ink: #231f20;
    --black: #0d0b0b;
    --white: #ffffff;
    --silver: #b5b5b5;
    --page: #ffffff;
  }
  * { margin: 0; padding: 0; box-sizing: border-box; }
  html, body { width: 1200px; height: 732px; overflow: hidden; background: var(--page); }
  body { position: relative; font-family: "Montserrat", Arial, sans-serif; }

  .card {
    position: absolute;
    width: 562px;
    height: 346px;
    overflow: hidden;
    box-shadow: 0 1px 4px rgba(0,0,0,0.25);
  }
  .card-front { left: 29px; top: 19px; background: var(--white); }
  .card-back-maroon { left: 606px; top: 19px; background: var(--maroon); }
  .card-back-black { left: 317px; top: 386px; background: var(--black); }

  .front-wave { position: absolute; inset: 0; }

  .brand {
    display: flex;
    align-items: center;
    gap: 10px;
    font-weight: 600;
    letter-spacing: 0.5px;
    white-space: nowrap;
  }
  .brand-dot { border-radius: 50%; flex: none; }

  .card-front .brand {
    position: absolute;
    left: 22px;
    top: 46px;
    font-size: 27px;
    color: var(--ink);
  }
  .card-front .brand-dot { width: 16px; height: 16px; background: var(--maroon); }

  .holder {
    position: absolute;
    left: 370px;
    top: 262px;
    color: var(--white);
  }
  .holder-name { font-size: 19px; font-weight: 400; }
  .holder-role { font-size: 12px; margin-top: 2px; padding-left: 40px; }

  .contact {
    position: absolute;
    left: 22px;
    top: 236px;
    color: var(--white);
    font-size: 12px;
    line-height: 17px;
    list-style: none;
  }

  .back-content {
    position: absolute;
    inset: 0;
    display: flex;
    flex-direction: column;
    align-items: center;
  }
  .back-content .brand { margin-top: 120px; font-size: 36px; }
  .back-content .brand-dot { width: 20px; height: 20px; }
  .card-back-maroon .brand { color: var(--ink); }
  .card-back-maroon .brand-dot { background: var(--white); }
  .card-back-black .brand { color: var(--white); }
  .card-back-black .brand-dot { background: var(--maroon); }

  .website {
    position: absolute;
    bottom: 42px;
    width: 100%;
    text-align: center;
    color: var(--white);
    font-size: 15px;
  }
</style>
</head>
<body>

  <section class="card card-front" aria-label="Business card front">
    <svg class="front-wave" width="562" height="346" viewBox="0 0 562 346" aria-hidden="true">
      <path d="M0,192 Q150,170 300,238 Q430,178 562,176" fill="none" stroke="var(--silver)" stroke-width="9"/>
      <path d="M0,210 Q150,190 300,256 Q430,198 562,194 L562,346 L0,346 Z" fill="var(--maroon)"/>
    </svg>

    <div class="brand"><span class="brand-dot"></span>Copperleaf Grill</div>

    <div class="holder">
      <p class="holder-name">Danielle Whitcomb</p>
      <p class="holder-role">Proprietor</p>
    </div>

    <ul class="contact">
      <li>318 Ferrand Street</li>
      <li>New Orleans, LA 70119</li>
      <li>Phone: 504.555.0147</li>
      <li>Cell: 225.555.0192</li>
      <li>Email: dwhitcomb@copperleaf-eats.com</li>
    </ul>
  </section>

  <section class="card card-back-maroon" aria-label="Business card back, maroon">
    <div class="back-content">
      <div class="brand"><span class="brand-dot"></span>Copperleaf Grill</div>
    </div>
    <p class="website">www.copperleaf-eats.com</p>
  </section>

  <section class="card card-back-black" aria-label="Business card back, black">
    <div class="back-content">
      <div class="brand"><span class="brand-dot"></span>Copperleaf Grill</div>
    </div>
    <p class="website">www.copperleaf-eats.com</p>
  </section>

</body>
</html>
```